Real Estate Flyer

I would like an A4 size flyer which has the same info 3 times and can be cut into three.
It will be used for letterbox drops for new listings (SELLING) and sold listings (SOLD). The flyer needs a heading (as above) and a space for a photo which is able to be changed for each new property. Needs to be blue, red and white. It also requires my photo, KLT logo, Marisse Thornbury logo and the following text:
"Are you considering selling? Call Marisse today for a complimentary market appraisal".
(KLT logo, Marisse Thornbury Sales Consultant logo and my photo can be found in uploaded files)
Industry/Entity Type
Real Estate
Look and feel

```html
<!DOCTYPE html>
<html lang="en">
<head>
<meta charset="utf-8">
<title>Marisse Thornbury – Real Estate Flyer</title>
<link rel="stylesheet" href="https://fonts.googleapis.com/css2?family=Didact+Gothic&family=Arimo:wght@400;700&display=swap">
<style>
  :root {
    --canvas-bg: #fbfbfb;
    --paper: #ffffff;
    --paper-edge: #d9d9d9;
    --blue-light: #0d9ce0;
    --blue-mid: #1174c4;
    --blue-deep: #2e3192;
    --red: #d8222b;
    --red-dark: #9c2a32;
    --white: #ffffff;
    --placeholder-text: #a3a3a3;
  }
  * { margin: 0; padding: 0; box-sizing: border-box; }
  html, body {
    width: 1200px;
    height: 1001px;
    overflow: hidden;
    background: var(--canvas-bg);
  }
  .flyer {
    position: absolute;
    left: 290px;
    top: 49px;
    width: 648px;
    height: 907px;
    background: var(--paper);
    border: 1px solid var(--paper-edge);
    overflow: hidden;
  }
  .flyer-shapes {
    position: absolute;
    inset: 0;
    width: 648px;
    height: 907px;
  }
  .brand-mark {
    position: absolute;
    left: 34px;
    top: 34px;
    width: 90px;
    display: flex;
    flex-direction: column;
    align-items: center;
    gap: 6px;
    color: var(--white);
    font-family: "Didact Gothic", sans-serif;
    font-size: 15px;
    line-height: 1.1;
    text-align: center;
  }
  .brand-mark .brand-dot {
    width: 46px;
    height: 46px;
    border-radius: 50%;
    background: var(--red);
  }
  .agent-heading {
    position: absolute;
    left: 135px;
    top: 38px;
    width: 405px;
    text-align: center;
    color: var(--white);
    font-family: "Didact Gothic", sans-serif;
  }
  .agent-name { font-size: 38px; line-height: 1.1; font-weight: 400; letter-spacing: 0.3px; }
  .agent-role { font-size: 26px; line-height: 1.05; }
  .agent-phone {
    margin-top: 6px;
    font-size: 19px;
    display: inline-flex;
    align-items: center;
    gap: 6px;
  }
  .agent-phone svg { width: 13px; height: 11px; }
  .agent-photo-frame {
    position: absolute;
    left: 539px;
    top: 12px;
    width: 94px;
    height: 127px;
    border: 4px solid var(--white);
    border-radius: 6px;
    padding: 2px 4px;
  }
  .agent-photo {
    width: 100%;
    height: 100%;
    background: linear-gradient(180deg, #d9d4cf 0%, #a99284 45%, #1e1d22 100%);
  }
  .property-photo {
    position: absolute;
    left: 0;
    top: 150px;
    width: 648px;
    height: 570px;
    display: flex;
    align-items: center;
    justify-content: center;
    color: var(--placeholder-text);
    font-family: "Arimo", sans-serif;
    font-size: 24px;
  }
  .appraisal-callout {
    position: absolute;
    left: 56px;
    top: 748px;
    color: var(--white);
    font-family: "Arimo", sans-serif;
    font-weight: 700;
  }
  .callout-question { font-size: 36.5px; line-height: 1.1; letter-spacing: 0.2px; }
  .callout-offer { font-size: 17px; line-height: 1.2; }
  .agency-badge {
    position: absolute;
    left: 540px;
    top: 855px;
    display: flex;
    align-items: center;
    gap: 5px;
    color: var(--white);
    font-family: "Arimo", sans-serif;
    font-weight: 700;
    font-size: 12px;
  }
  .agency-badge .badge-square {
    width: 10px;
    height: 10px;
    background: var(--red);
  }
</style>
</head>
<body>
  <main class="flyer">
    <svg class="flyer-shapes" viewBox="0 0 648 907" aria-hidden="true">
      <defs>
        <linearGradient id="header-blue" x1="0" y1="0" x2="0" y2="1">
          <stop offset="0" stop-color="#2250a4"/>
          <stop offset="1" stop-color="#0aa2e4"/>
        </linearGradient>
        <linearGradient id="footer-blue" x1="0" y1="0" x2="0" y2="1">
          <stop offset="0" stop-color="#0f88d2"/>
          <stop offset="1" stop-color="#2e3192"/>
        </linearGradient>
      </defs>
      <!-- header -->
      <path d="M0 0 H648 V167 Q324 121 0 167 Z" fill="url(#header-blue)"/>
      <path d="M0 167 Q324 121 648 167 V188 Q324 108 0 188 Z" fill="var(--red-dark)"/>
      <path d="M0 167 Q324 121 648 167 L648 171 Q324 127 0 171 Z" fill="var(--red)"/>
      <!-- footer -->
      <path d="M0 671 Q324 761 648 671 V696 Q324 746 0 696 Z" fill="var(--red-dark)"/>
      <path d="M0 690 Q324 752 648 690 V696 Q324 746 0 696 Z" fill="var(--red)"/>
      <path d="M0 696 Q324 746 648 696 V907 H0 Z" fill="url(#footer-blue)"/>
    </svg>

    <div class="brand-mark">
      <span class="brand-dot"></span>
      <span>Marisse<br>Thornbury</span>
    </div>

    <header class="agent-heading">
      <h1 class="agent-name">Marisse Thornbury</h1>
      <p class="agent-role">Sales Consultant</p>
      <p class="agent-phone">
        <svg viewBox="0 0 13 11" aria-hidden="true"><path d="M1 3 Q6.5 -1 12 3 L11 5 L9 4.5 L8.6 3.2 Q6.5 2.6 4.4 3.2 L4 4.5 L2 5 Z M3 6 H10 L11.5 10.5 H1.5 Z" fill="#fff"/></svg>
        0412558091
      </p>
    </header>

    <div class="agent-photo-frame">
      <div class="agent-photo" role="img" aria-label="Portrait photo of the sales consultant"></div>
    </div>

    <section class="property-photo" role="img" aria-label="Property photo area, replaced for each listing">
      space for image property
    </section>

    <section class="appraisal-callout">
      <p class="callout-question">“Are you considering selling?</p>
      <p class="callout-offer">Call Marisse today for a complimentary market appraisal".</p>
    </section>

    <div class="agency-badge">
      <span class="badge-square"></span>
      <span>KLT</span>
    </div>
  </main>
</body>
</html>
```